Adult dating site banners and payment page concepts

We need an overhaul done on our banners, as well as rebranding our packages. We have uploaded a full description of what we need doing, we are not looking for you do do all of them right now. We are looking for a concept for one site banner, one version of the payment page, and one affiliate banner. We will then pay the winner to do the rest of the design work we need to get them all done, but we have uploaded all the bits we will eventually need.

• Banner design brief
• We are looking for a new design for all of our upgrade banners for our adult dating swingers sites as well as our payment pages so they need to appeal to men, women, and couples. We are looking for something fun and sexy that really looks nice on mobile and desktop.
• Important design notes banners
• 1. Where you see the word “Extras” we are changing it to a package called “Plus, this can be the word Plus or the + symbol, or both”, we are looking for a design for this.
• 2. Where you see the word “Premium” we are now calling it “Supporter” so that needs some nice font or design as well.
• 3. We would like the offers to jump out at you with the discounts etc.
• 4. The banners need to be able to work on our different sites on the following colours:
• South Africa #7e0202
• UK #0d72ba
• Canada #147eab
• Ireland #003a15
• Australia #272f47
• New Zealand #446160
• Payment pages
• 1. We would like to keep them clean as most of our users are on mobile
• 2. But if you think they can be improved to help with conversion rates we would like to see it.
• Affiliate banners
• We also advertise our sites on other websites using geo-targeted banners; we need to tempt people to click through. The ones we have right now are not animated and we like the idea of that, something saucy and sexy but not porn related. We would like these to be re designed to be something sexier that grabs your attention.

```html
<!DOCTYPE html>
<html lang="en">
<head>
<meta charset="utf-8">
<title>Upgrade Now</title>
<link rel="stylesheet" href="https://fonts.googleapis.com/css2?family=Lato:wght@400;700&display=swap">
<style>
  :root {
    --page-bg: #e8eaed;
    --card-bg: #ffffff;
    --title-red: #8c1616;
    --text-dark: #222222;
    --text-mid: #444444;
    --line: #e6e6e6;
    --supporter-blue: #4596c8;
    --plus-green: #3bb14c;
    --tick-green: #2c7a30;
    --badge-blue: #1e78c8;
    --badge-border: #e4e4e4;
  }
  * { box-sizing: border-box; margin: 0; padding: 0; }
  html, body {
    width: 1200px; height: 1200px; overflow: hidden;
    background: var(--page-bg);
    font-family: "Lato", Arial, sans-serif;
    color: var(--text-dark);
  }
  .upgrade-modal {
    position: absolute; left: 50px; top: 153px;
    width: 1100px; height: 894px;
    background: var(--card-bg);
    box-shadow: 0 18px 40px rgba(0,0,0,0.18);
  }
  .modal-close {
    position: absolute; right: 8px; top: 4px;
    font-size: 18px; color: #c4c4c4;
  }
  .modal-title {
    position: absolute; top: 24px; left: 0; right: 0;
    text-align: center; font-weight: 400; font-size: 31px;
    color: var(--title-red);
  }
  .payment-plan { position: absolute; left: 133px; top: 112px; }
  .payment-plan-label { font-size: 22px; color: var(--title-red); margin-bottom: 8px; }
  .plan-toggle {
    display: flex; width: 240px; height: 37px;
    border: 1px solid #d4d4d4; border-radius: 3px; overflow: hidden;
  }
  .plan-toggle span {
    flex: 1; display: flex; align-items: center; justify-content: center;
    font-size: 17px; color: var(--text-dark);
  }
  .plan-toggle .is-active { background: var(--plus-green); color: #fff; }

  .feature-labels { position: absolute; left: 287px; top: 249px; width: 293px; }
  .feature-labels li {
    list-style: none; height: 48px; display: flex; align-items: center;
    padding-left: 12px; font-size: 13.5px; color: var(--text-mid);
    border-bottom: 1px solid var(--line);
  }
  .feature-labels { left: 131px; }

  .plan-column {
    position: absolute; top: 92px; width: 250px;
    box-shadow: 0 2px 6px rgba(0,0,0,0.14);
    background: #fff;
  }
  .plan-column.supporter { left: 436px; --plan-colour: var(--supporter-blue); }
  .plan-column.plus { left: 705px; --plan-colour: var(--plus-green); }
  .plan-header {
    height: 157px; background: var(--plan-colour); color: #fff;
    text-align: center; position: relative;
  }
  .plan-name { position: absolute; top: 12px; left: 0; right: 0; font-size: 24px; }
  .plan-price { position: absolute; top: 55px; left: 0; right: 0; font-size: 36px; }
  .plan-period { position: absolute; top: 121px; left: 0; right: 0; font-size: 16px; }
  .plan-features li {
    list-style: none; height: 48px; display: flex; align-items: center; justify-content: center;
    border-bottom: 1px solid var(--line); font-size: 14px; font-weight: 700; color: var(--text-dark);
  }
  .plan-features .not-included { font-weight: 400; color: #666; }
  .tick { width: 13px; height: 11px; }
  .plan-button {
    height: 66px; background: var(--plan-colour); color: #fff;
    display: flex; align-items: center; justify-content: center; font-size: 19px;
  }

  .trust-badges { position: absolute; top: 825px; left: 25px; display: flex; gap: 24px; }
  .trust-badge {
    width: 243px; height: 51px; border: 1px solid var(--badge-border);
    display: flex; align-items: center; justify-content: center; gap: 10px;
    font-size: 15px; color: var(--text-dark);
  }
  .trust-badge svg { width: 17px; height: 17px; fill: var(--badge-blue); }
</style>
</head>
<body>
<svg width="0" height="0" style="position:absolute">
  <symbol id="tick" viewBox="0 0 13 11"><path d="M1 6 L5 9.5 L12 1.5" fill="none" stroke="#2c7a30" stroke-width="2.4"/></symbol>
</svg>

<section class="upgrade-modal">
  <span class="modal-close">×</span>
  <h1 class="modal-title">Upgrade Now</h1>

  <div class="payment-plan">
    <p class="payment-plan-label">Payment plan</p>
    <div class="plan-toggle"><span class="is-active">Monthly</span><span>Yearly</span></div>
  </div>

  <ul class="feature-labels">
    <li>Cancel at any time</li>
    <li>Unlimited Messaging</li>
    <li>Adult Photos and Videos</li>
    <li>Full Chatroom Access</li>
    <li>Send Statuses to Friends &amp; Followers</li>
    <li>Chatroom Webcams</li>
    <li>Send Statuses to Matches</li>
    <li>Multiple Chat Access for Couples</li>
    <li>HD Photos and Videos</li>
    <li>See Who's Looked at Your Profile</li>
  </ul>

  <div class="plan-column supporter">
    <div class="plan-header">
      <p class="plan-name">Supporter</p>
      <p class="plan-price">R134,95</p>
      <p class="plan-period">monthly</p>
    </div>
    <ul class="plan-features">
      <li><svg class="tick"><use href="#tick"/></svg></li>
      <li><svg class="tick"><use href="#tick"/></svg></li>
      <li><svg class="tick"><use href="#tick"/></svg></li>
      <li><svg class="tick"><use href="#tick"/></svg></li>
      <li><svg class="tick"><use href="#tick"/></svg></li>
      <li>2</li>
      <li class="not-included">-</li>
      <li class="not-included">-</li>
      <li class="not-included">-</li>
      <li class="not-included">-</li>
    </ul>
    <div class="plan-button">Upgrade Now</div>
  </div>

  <div class="plan-column plus">
    <div class="plan-header">
      <p class="plan-name">Plus</p>
      <p class="plan-price">R154,95</p>
      <p class="plan-period">monthly</p>
    </div>
    <ul class="plan-features">
      <li><svg class="tick"><use href="#tick"/></svg></li>
      <li><svg class="tick"><use href="#tick"/></svg></li>
      <li><svg class="tick"><use href="#tick"/></svg></li>
      <li><svg class="tick"><use href="#tick"/></svg></li>
      <li><svg class="tick"><use href="#tick"/></svg></li>
      <li>7</li>
      <li><svg class="tick"><use href="#tick"/></svg></li>
      <li><svg class="tick"><use href="#tick"/></svg></li>
      <li><svg class="tick"><use href="#tick"/></svg></li>
      <li><svg class="tick"><use href="#tick"/></svg></li>
    </ul>
    <div class="plan-button">Upgrade Now</div>
  </div>

  <div class="trust-badges">
    <div class="trust-badge">
      <svg viewBox="0 0 16 16"><rect x="2" y="7" width="12" height="9" rx="1"/><path d="M4.5 7 V5 a3.5 3.5 0 0 1 7 0 V7" fill="none" stroke="#1e78c8" stroke-width="2"/></svg>
      100% Secure
    </div>
    <div class="trust-badge">
      <svg viewBox="0 0 16 16"><rect x="4" y="1" width="8" height="5" rx="1"/><rect x="1" y="6" width="14" height="1.6"/><circle cx="5" cy="10" r="2"/><circle cx="11" cy="10" r="2"/><path d="M2 16 Q8 11 14 16 Z"/></svg>
      Discrete Billing
    </div>
    <div class="trust-badge">
      <svg viewBox="0 0 16 16"><path d="M8 0.5 L14.5 3 V8 C14.5 12 11.5 14.5 8 15.5 C4.5 14.5 1.5 12 1.5 8 V3 Z M8 2.5 V13.5 C10.5 12.6 12.5 10.7 12.5 8 V4.3 Z" fill-rule="evenodd"/></svg>
      Data Protection
    </div>
    <div class="trust-badge">
      <svg viewBox="0 0 16 16"><path d="M10 0 L3 9 H7.5 L6 16 L13 6.5 H8.5 Z"/></svg>
      Instant Access
    </div>
  </div>
</section>
</body>
</html>
```